Velkano Holdings Ltd - An invesmtent & trading company needs a web design

We need a web design for our company based in Cyprus. The company was founded in 2009. We have continuously grown and now invest & trade all over the world.

Velkano Holdings ltd. specializes in the buying and selling of crude oil, precious metals and the investment in properties.

We know that trust is of the utmost importance when it comes to business and the design should communicate this to prospective business partners. Find attached the company logo. The colour scheme for the website should use similar colours and ideally incorporate the logo in some shape or form as well.

Target Market(s)

Oil Traders, Metall Traders, Property Investments

Industry/Entity Type

Trade

Coding

Coded - Design and coding required

Number of Pages Required

4 page

Font styles to use
Sans Serif

Requirements
Must have
• Mainpage,
• About Us
• Partners
• Legal Notice

```html
<!DOCTYPE html>
<html lang="en">
<head>
<meta charset="utf-8">
<title>Velkano Holdings Ltd</title>
<link href="https://fonts.googleapis.com/css2?family=Open+Sans:wght@400;600;700&display=swap" rel="stylesheet">
<style>
:root{
  --bg:#2b2b2b;
  --bg-dark:#1c1c1c;
  --panel:#232323;
  --accent:#2b93d6;
  --text:#e6e6e6;
  --muted:#a9a9a9;
  --partner:#d4d4d4;
}
*{box-sizing:border-box;margin:0;padding:0}
html,body{width:839px;height:1200px;overflow:hidden}
body{background:var(--bg);font-family:"Open Sans",Arial,sans-serif;color:var(--text);position:relative}
.site-header{position:absolute;left:0;top:0;width:839px;height:58px;background:var(--bg-dark)}
.brand{position:absolute;left:44px;top:14px;display:flex;align-items:center;gap:8px}
.brand-mark{width:26px;height:26px;background:var(--accent)}
.brand-name{font-size:13px;font-weight:700;color:var(--accent);line-height:13px;text-transform:uppercase;letter-spacing:.5px}
.main-nav{position:absolute;left:304px;top:22px;display:flex;gap:14px;font-size:9px;font-weight:600;text-transform:uppercase}
.main-nav a{color:var(--text);text-decoration:none}
.main-nav a.active{background:#fff;color:#111;padding:1px 4px}
.social{position:absolute;right:20px;top:18px;display:flex;gap:6px}
.social span{width:18px;height:18px;border-radius:50%;background:#8c8c8c}
.hero{position:absolute;left:48px;top:92px;width:743px;height:360px;border:2px solid var(--accent);
  background:linear-gradient(180deg,#6d7378 0%,#9a8f82 45%,#6a5f55 100%)}
.hero-text{position:absolute;left:40px;right:40px;top:200px;text-align:center;font-size:19px;line-height:27px;color:#fff}
.about{position:absolute;left:48px;top:474px;width:743px;text-align:center}
.section-title{font-size:19px;color:var(--accent);font-weight:400;text-transform:uppercase}
.about p{margin-top:8px;font-size:9px;line-height:13px;color:var(--muted);text-align:left}
.btn-outline{display:inline-block;margin-top:14px;border:1px solid #ccc;color:#fff;font-size:11px;padding:5px 14px}
.specialize{position:absolute;left:48px;top:660px;width:548px}
.bar{height:18px;background:var(--bg-dark);border-bottom:2px solid var(--accent);text-align:center;font-size:9px;font-weight:700;line-height:17px;text-transform:uppercase}
.cards{display:flex;gap:12px;margin-top:6px}
.card{position:relative;width:175px;height:242px;border-bottom:3px solid var(--accent)}
.card-photo{position:absolute;inset:0}
.oil{background:linear-gradient(180deg,#8f9fac,#3f4850)}
.metal{background:linear-gradient(180deg,#5d6166,#2e3033)}
.property{background:linear-gradient(180deg,#7aa2c4,#3b5a70)}
.card-icon{position:absolute;left:62px;top:34px;width:50px;height:50px;border:3px solid #fff;border-radius:50%}
.card-title{position:absolute;left:0;right:0;top:146px;text-align:center;font-size:13px;font-weight:700;line-height:15px;text-transform:uppercase;color:#fff}
.card-btn{position:absolute;left:62px;top:206px;width:52px;height:14px;background:var(--bg-dark);font-size:7px;line-height:14px;text-align:center;color:#fff}
.contact{position:absolute;left:612px;top:660px;width:179px;height:266px;background:var(--panel)}
.contact .bar{margin-bottom:8px}
.contact p{font-size:7px;line-height:10px;color:var(--muted);padding:0 10px}
.field{margin:6px 10px 0;height:18px;background:#fff;font-size:7px;color:#888;padding:4px}
.field.msg{height:76px}
.send{margin:8px 10px;width:40px;height:14px;background:#fff;color:#111;font-size:7px;text-align:center;line-height:14px}
.partners{position:absolute;left:48px;top:966px;width:743px;text-align:center}
.partner-row{display:flex;justify-content:space-between;align-items:center;margin-top:30px;padding:0 10px}
.partner{display:flex;align-items:center;gap:7px;font-size:17px;font-weight:600;color:var(--partner)}
.partner-mark{width:14px;height:14px;background:#555}
.site-footer{position:absolute;left:0;top:1082px;width:839px;height:118px;background:var(--bg-dark);border-top:2px solid var(--accent)}
.foot-col{position:absolute;top:16px;font-size:8px;line-height:11px;color:var(--muted)}
.foot-col h4{color:#fff;font-size:8px;margin-bottom:3px}
.foot-social{display:flex;gap:4px;margin-top:3px}
.foot-social span{width:13px;height:13px;border-radius:50%;background:#8c8c8c}
.foot-brand{position:absolute;left:578px;top:20px;display:flex;align-items:center;gap:5px}
.foot-brand .brand-mark{width:16px;height:16px}
.foot-brand .brand-name{font-size:9px}
.copyright{position:absolute;left:598px;top:44px;font-size:6px;color:var(--muted)}
</style>
</head>
<body>
<header class="site-header">
  <div class="brand"><span class="brand-mark"></span><span class="brand-name">Velkano<br>Holdings Ltd.</span></div>
  <nav class="main-nav"><a class="active">Home</a><a>About Us</a><a>Partners</a><a>Legal Notice</a><a>Contact</a></nav>
  <div class="social"><span></span><span></span><span></span><span></span></div>
</header>

<section class="hero" role="img" aria-label="City skyline photograph of the company's home city">
  <p class="hero-text">Velkano Holdings ltd. specializes in the buying and selling of crude oil, precious metals and the investment in properties.</p>
</section>

<section class="about">
  <h2 class="section-title">About Velkano Holdings Ltd.</h2>
  <p>Founded in 2009 and based in Cyprus, Velkano Holdings has grown steadily and now invests and trades all over the world. We work with oil traders, metal traders and property investors who value reliable partners and clear agreements. Our team combines long market experience with careful risk management, so every deal is handled with the same attention to detail. We believe trust is the foundation of any lasting business relationship, and we earn it through transparency, discretion and results. From crude oil cargoes to precious metals and real estate portfolios, we build long term value for our partners and clients across many regions and markets every year.</p>
  <span class="btn-outline">Discover More</span>
</section>

<section class="specialize">
  <div class="bar">We specialize in</div>
  <div class="cards">
    <div class="card"><div class="card-photo oil" role="img" aria-label="Oil refinery photograph"></div><span class="card-icon"></span><div class="card-title">Buying &amp; Selling<br>of Crude Oil</div><div class="card-btn">Learn More</div></div>
    <div class="card"><div class="card-photo metal" role="img" aria-label="Stacked coins photograph"></div><span class="card-icon"></span><div class="card-title">Buying &amp; Selling<br>Precious Metals</div><div class="card-btn">Learn More</div></div>
    <div class="card"><div class="card-photo property" role="img" aria-label="Office towers photograph"></div><span class="card-icon"></span><div class="card-title">Investments<br>in Properties</div><div class="card-btn">Learn More</div></div>
  </div>
</section>

<aside class="contact">
  <div class="bar">Contact Us</div>
  <p>Please feel free to use the form below and we will reply soon.</p>
  <div class="field">Name</div>
  <div class="field">Phone Number</div>
  <div class="field">Email Address</div>
  <div class="field msg">Your Message</div>
  <div class="send">Submit</div>
</aside>

<section class="partners">
  <h2 class="section-title">Our Partners</h2>
  <div class="partner-row">
    <span class="partner"><span class="partner-mark"></span>Corvane</span>
    <span class="partner"><span class="partner-mark"></span>Tellwick</span>
    <span class="partner"><span class="partner-mark"></span>Norbeam</span>
    <span class="partner"><span class="partner-mark"></span>Quillary</span>
    <span class="partner"><span class="partner-mark"></span>Ostrava Link</span>
  </div>
</section>

<footer class="site-footer">
  <div class="foot-col" style="left:132px"><h4>Quick Links</h4>Home<br>About Us<br>Partners<br>Legal Notice</div>
  <div class="foot-col" style="left:240px"><h4>Contact</h4>Limassol, Cyprus<br>info@velkano-example.com<br>+357 00 000 000<br>Mon to Fri</div>
  <div class="foot-col" style="left:420px"><h4>Follow Us</h4><div class="foot-social"><span></span><span></span><span></span><span></span></div></div>
  <div class="foot-brand"><span class="brand-mark"></span><span class="brand-name">Velkano Holdings Ltd.</span></div>
  <div class="copyright">© 2009 Velkano Holdings Ltd.</div>
</footer>
</body>
</html>
```